Company business card

We need a new business card design. We are IT company which is specialized for outsourcing of operations hardware and software (specially Quorvane, we are a partner), developing custom applications and web applications, BPM solutions, auditing hw and sw. actually design was attached. But we need completely NEW.

Business

```html
<!DOCTYPE html>
<html lang="en">
<head>
<meta charset="utf-8">
<title>BRIXON business card</title>
<link rel="stylesheet" href="https://fonts.googleapis.com/css2?family=Montserrat:wght@700&family=Open+Sans:wght@400;600;700&display=swap">
<style>
  :root {
    --backdrop: #dcdcdc;
    --brand-blue: #2f7fc1;
    --card-white: #ffffff;
    --ink-blue: #2c7bbf;
  }
  html, body {
    margin: 0;
    width: 1200px;
    height: 1000px;
    overflow: hidden;
    background: var(--backdrop);
  }
  .canvas {
    position: relative;
    width: 1200px;
    height: 1000px;
  }
  .card {
    position: absolute;
    width: 560px;
    height: 320px;
    box-shadow: 0 6px 18px rgba(0,0,0,0.12);
  }
  .card--front {
    left: 90px;
    top: 130px;
    background: var(--brand-blue);
    display: flex;
    align-items: center;
    justify-content: center;
  }
  .card--back {
    left: 550px;
    top: 540px;
    background: var(--card-white);
  }
  .brand {
    display: flex;
    align-items: center;
    gap: 16px;
  }
  .brand__square {
    width: 66px;
    height: 66px;
    display: block;
  }
  .brand__name {
    font-family: "Montserrat", sans-serif;
    font-weight: 700;
    font-size: 40px;
    letter-spacing: 1px;
    line-height: 1;
  }
  .card--front .brand__square { background: var(--card-white); }
  .card--front .brand__name { color: var(--card-white); }
  .card--back .brand__square { background: var(--ink-blue); }
  .card--back .brand__name { color: var(--ink-blue); }

  .identity {
    position: absolute;
    left: 50px;
    top: 70px;
    font-family: "Open Sans", sans-serif;
    color: var(--ink-blue);
  }
  .person {
    margin-top: 18px;
  }
  .person__name {
    font-weight: 700;
    font-size: 26px;
    line-height: 1.1;
  }
  .person__role {
    font-weight: 700;
    font-size: 11px;
    letter-spacing: 0.5px;
    margin-top: 2px;
    text-align: right;
  }
  .contact {
    margin-top: 14px;
    font-size: 13px;
    line-height: 1.7;
  }
  .company {
    position: absolute;
    left: 370px;
    top: 70px;
    font-family: "Open Sans", sans-serif;
    font-size: 13px;
    color: var(--ink-blue);
    line-height: 1.45;
  }
  .company__web { margin-bottom: 40px; }
</style>
</head>
<body>
<main class="canvas">
  <section class="card card--front" aria-label="Card front">
    <div class="brand">
      <span class="brand__square"></span>
      <span class="brand__name">BRIXON</span>
    </div>
  </section>

  <section class="card card--back" aria-label="Card back">
    <div class="identity">
      <div class="brand">
        <span class="brand__square"></span>
        <span class="brand__name">BRIXON</span>
      </div>
      <div class="person">
        <div class="person__name">Marek Dolinský</div>
        <div class="person__role">CEO</div>
      </div>
      <div class="contact">
        <div class="contact__email">marek.dolinsky@brixon.sk</div>
        <div class="contact__phone">+421 (0) 900 555 018</div>
      </div>
    </div>
    <div class="company">
      <div class="company__web">www.brixon.sk</div>
      <div class="company__name">BRIXON s.r.o.</div>
      <div class="company__street">Lipová 12</div>
      <div class="company__city">811 02 Bratislava</div>
    </div>
  </section>
</main>
</body>
</html>
```